Wed site for biomedical device startup

We need a generic website for a medical device startup. I will provide examples below of websites from other companies that can serve as models for what we are looking for. The startup is for a device that can non invasively measure blood flow in the brain using light. The application is to detect the type of stroke someone is having before they get to the hospital so treatment can be started right away. This saves patients upto hours of delayed treatment. Patients will be able to recover from stroke much better and faster as a result. I have attached an AI generated illustration of what the device will ultimately look like for reference.

https://www.brightvalemedical.com
https://quintavex.com

Target Market(s)

Biomedical, medical device, investors of biomedical device startups

Industry/Entity Type

Biomedical

Coding

Coded - Design and coding required

Number of Pages Required

4 page

Requirements
Must have
• same section and section headings as example websites listed above
Nice to have
• similar to example websites listed above. Prefer a darker website over a lighter one. Perhaps dark blues to go with logo colors. A moving background image element at top of landing page could be cool. Something indicative of heartbeat, or neurons, or blood flow.

```html
<!DOCTYPE html>
<html lang="en">
<head>
<meta charset="utf-8">
<title>LUMIVA — Improving the Future for the Smallest Patients</title>
<link rel="stylesheet" href="https://fonts.googleapis.com/css2?family=Orbitron:wght@400;700;800&family=Roboto:wght@400;500&display=swap">
<style>
  :root {
    --navy: #07063f;
    --navy-deep: #05042f;
    --cyan: #1fd1e6;
    --cyan-soft: #14c4dc;
    --purple: #8a3fd6;
    --violet: #6a2fc9;
    --blue: #2b3fc4;
    --white: #ffffff;
    --ink: #0b0a4a;
    --field-text: #5a5a6e;
    --btn-grad: linear-gradient(90deg, #8a3fd6 0%, #4f7fe0 60%, #1fd1e6 100%);
  }
  * { box-sizing: border-box; margin: 0; padding: 0; }
  html, body { width: 1200px; height: 3989px; overflow: hidden; }
  body {
    position: relative;
    background: var(--navy);
    color: var(--white);
    font-family: "Roboto", Arial, sans-serif;
  }
  .abs { position: absolute; }

  .heading {
    position: absolute;
    font-family: "Orbitron", sans-serif;
    font-weight: 400;
    font-size: 36px;
    line-height: 46px;
    letter-spacing: 0.5px;
    text-transform: uppercase;
    color: var(--white);
  }
  .heading strong { font-weight: 800; color: var(--cyan); }
  .heading strong.white { color: var(--white); }
  .heading strong.ink { color: var(--ink); }

  .body-copy {
    position: absolute;
    font-size: 12.5px;
    line-height: 24px;
    text-align: justify;
    color: var(--white);
  }

  .btn {
    position: absolute;
    height: 52px;
    border-radius: 26px;
    background: var(--btn-grad);
    color: var(--ink);
    font-size: 15px;
    font-weight: 500;
    text-transform: uppercase;
    display: flex;
    align-items: center;
    justify-content: center;
    text-decoration: none;
  }
  .btn-light { background: var(--white); color: var(--purple); }
  .btn-dark { background: var(--ink); color: var(--white); }

  /* header */
  .brand {
    position: absolute;
    display: flex;
    align-items: center;
    gap: 14px;
    font-family: "Orbitron", sans-serif;
    font-weight: 400;
    font-size: 44px;
    color: var(--white);
    letter-spacing: 2px;
  }
  .brand-dot {
    width: 62px; height: 62px; border-radius: 50%;
    background: var(--btn-grad);
  }
  .main-nav {
    position: absolute; top: 52px; left: 636px;
    display: flex; gap: 30px; font-size: 13px;
    text-transform: uppercase;
  }
  .main-nav a { color: var(--white); text-decoration: none; display: flex; align-items: center; gap: 8px; }
  .nav-dot { width: 15px; height: 15px; border-radius: 50%; background: var(--btn-grad); }

  .hero-art {
    left: 0; top: 150px; width: 1200px; height: 420px;
    background:
      radial-gradient(ellipse 55% 18% at 50% 50%, rgba(31,209,230,.35), transparent 70%),
      linear-gradient(90deg, rgba(20,100,200,.0), rgba(31,209,230,.25) 30%, rgba(180,80,200,.2) 55%, rgba(31,209,230,.25) 80%, rgba(20,100,200,0));
    mask-image: linear-gradient(180deg, transparent 0%, #000 35%, #000 65%, transparent 100%);
  }
  .slider-dots { left: 1132px; top: 274px; display: flex; flex-direction: column; gap: 17px; }
  .slider-dots span { width: 7px; height: 7px; border-radius: 50%; background: var(--white); }
  .slider-dots span.active { background: var(--cyan); }

  .network-bg {
    left: 0; width: 1200px;
    background: radial-gradient(ellipse 60% 60% at 50% 100%, rgba(60,70,170,.35), transparent 70%);
  }

  .help-band {
    left: 9px; top: 1022px; width: 1182px; height: 568px;
    background: linear-gradient(100deg, #5a22b8 0%, #3a2cc0 45%, #2a3ec8 100%);
  }
  .help-art {
    left: 560px; top: 1110px; width: 631px; height: 480px;
    background: radial-gradient(ellipse 50% 50% at 55% 55%, rgba(90,200,255,.7), rgba(60,110,240,.5) 55%, transparent 75%);
  }

  .ring {
    position: absolute; border-radius: 50%;
    background: linear-gradient(180deg, #2fb6e6 0%, #5b6fe0 55%, #8a3fd6 100%);
    padding: 22px;
  }
  .ring-inner { width: 100%; height: 100%; border-radius: 50%; }
  .ring-inner.neuron { background: radial-gradient(circle at 45% 45%, #2f7fe0 0%, #123080 45%, #0a1548 100%); }
  .ring-inner.atom { background: radial-gradient(circle at 50% 50%, #c88a70 0%, #6a6fc8 35%, #3b44a8 75%, #2a2f8a 100%); }

  .standards { left: 0; top: 2661px; width: 1200px; height: 410px; }
  .std-left { background: linear-gradient(110deg, #6a2fc9 0%, #8a3fd6 60%, #9b45d9 100%); }
  .std-copy { font-size: 12.5px; line-height: 24px; position: absolute; width: 300px; }

  .contact-field {
    position: absolute; background: var(--white); color: var(--field-text);
    font-size: 15px; padding: 17px 21px 0; height: 52px;
  }
  .contact-fade {
    left: 0; top: 3480px; width: 1200px; height: 180px;
    background: linear-gradient(90deg, transparent 15%, rgba(31,209,230,.25) 35%, transparent 50%, rgba(31,209,230,.2) 75%, transparent 95%);
    mask-image: linear-gradient(180deg, transparent, #000);
  }

  .site-footer {
    left: 0; top: 3660px; width: 1200px; height: 329px;
    background: radial-gradient(ellipse 70% 80% at 50% 100%, #0d1560 0%, var(--navy-deep) 70%);
  }
  .footer-nav {
    position: absolute; top: 3818px; left: 0; width: 1200px;
    display: flex; justify-content: center; gap: 31px; font-size: 13px;
  }
  .footer-nav a { color: var(--white); text-decoration: none; }
  .copyright { top: 3857px; left: 0; width: 1200px; text-align: center; font-size: 13px; }
  .social { top: 3896px; left: 554px; display: flex; gap: 12px; }
  .social span { width: 40px; height: 40px; border-radius: 50%; border: 1.5px solid var(--white); display: block; }
  .social span.filled { background: var(--btn-grad); border: none; }
  .chat-btn {
    left: 1081px; top: 3632px; width: 66px; height: 66px; border-radius: 50%;
    background: #2f8fe0; display: flex; align-items: center; justify-content: center;
  }
</style>
</head>
<body>

<!-- Header -->
<div class="brand" style="left:144px;top:27px;"><span class="brand-dot"></span>LUMIVA</div>
<nav class="main-nav">
  <a href="#"><span class="nav-dot"></span>Home</a>
  <a href="#">About</a>
  <a href="#">Technology</a>
  <a href="#">Press</a>
  <a href="#">Contact</a>
</nav>

<!-- Hero -->
<div class="abs hero-art" role="img" aria-label="Flowing multicolour light wave suggesting brain blood flow"></div>
<h1 class="heading" style="left:572px;top:162px;">Improving the future<br><strong>for the smallest</strong><br>patients</h1>
<a class="btn" href="#" style="left:573px;top:326px;width:250px;">Explore our solutions</a>
<div class="abs slider-dots"><span></span><span class="active"></span><span></span></div>

<!-- About -->
<div class="abs network-bg" style="top:780px;height:240px;" role="img" aria-label="Faint network of glowing lines"></div>
<h2 class="heading" style="left:145px;top:667px;">About<br><strong>our mission</strong></h2>
<p class="body-copy" style="left:497px;top:671px;width:558px;">Sed ut perspiciatis unde omnis iste natus error sit voluptatem accusantium doloremque laudantium, totam rem aperiam, eaque ipsa quae ab illo inventore veritatis et quasi architecto beatae vitae dicta sunt explicabo. Nemo enim ipsam voluptatem quia voluptas sit aspernatur aut odit aut fugit, sed quia consequuntur magni dolores eos qui ratione voluptatem sequi nesciunt. Neque porro quisquam est, qui dolorem ipsum quia dolor sit amet, consecteturemo enim ipsam voluptatem quia voluptas sit aspernatur aut odit aut fugit, sed quia consequuntur magni dolores eoemo enim ipsam voluptatemt odit aut fugit, sed quuntur magni dolore.</p>
<a class="btn" href="#" style="left:497px;top:868px;width:148px;">Read more</a>

<!-- How we help -->
<section class="abs help-band"></section>
<div class="abs help-art" role="img" aria-label="Glowing blue circuit-patterned brain"></div>
<h2 class="heading" style="left:145px;top:1124px;">How <strong class="white">we help</strong></h2>
<p class="body-copy" style="left:146px;top:1192px;width:352px;">Sed ut perspiciatis unde omnis iste natus error sit voluptatem accusantium doloremque laudantium, totam rem aperiam, eaque ipsa quae ab illo inventore veritatis et quasi architecto beatae vitae dicta sunt explicabo. Nemo enim ipsam voluptatem quia voluptas sit aspernatur aut odit aut fugit, sed quia consequuntur magni dolores eos qui ratione voluptatem sequi nesciunt. Neque porro quisquam est, qui dolorem ipsum quia dolor sit amet, consecteturemo enim</p>
<a class="btn" href="#" style="left:146px;top:1412px;width:148px;">Read more</a>

<!-- Diagnostics -->
<div class="ring" style="left:143px;top:1672px;width:410px;height:410px;">
  <div class="ring-inner neuron" role="img" aria-label="Glowing blue neuron cell"></div>
</div>
<h2 class="heading" style="left:607px;top:1706px;">Diagnostics &amp;<br><strong>biosensors</strong></h2>
<p class="body-copy" style="left:608px;top:1815px;width:447px;">Sed ut perspiciatis unde omnis iste natus error sit voluptatem accusantium doloremque laudantium, totam rem aperiam, eaque ipsa quae ab illo inventore veritatis et quasi architecto beatae vitae dicta sunt explicabo. Nemo enim ipsam voluptatem quia voluptas sit aspernatur aut odit aut fugit, sed quia consequuntur magni dolores eos qui ratione voluptatem sequi porro qurem ipsum quia dolor sit amet, consecteturemo enim</p>
<a class="btn" href="#" style="left:608px;top:1985px;width:148px;">Read more</a>

<!-- Biotech devices -->
<div class="abs network-bg" style="top:2420px;height:240px;" role="img" aria-label="Faint network of glowing lines"></div>
<h2 class="heading" style="left:142px;top:2218px;">Biotech <strong>devices</strong></h2>
<p class="body-copy" style="left:144px;top:2282px;width:435px;">Sed ut perspiciatis unde omnis iste natus error sit voluptatem accusantium doloremque laudantium, totam rem aperiam, eaque ipsa quae ab illo inventore veritatis et quasi architecto beatae vitae dicta sunt explicabo. Nemo enim ipsam voluptatem quia voluptas sit aspernatur aut odit aut fugit, sed quia consequuntur magni dolores eos qui ratione voluptatem sequi porro qurem ipsum quia dolor sit amet, consecteturemo enim</p>
<a class="btn" href="#" style="left:144px;top:2451px;width:148px;">Read more</a>
<div class="ring" style="left:631px;top:2160px;width:410px;height:410px;">
  <div class="ring-inner atom" role="img" aria-label="Molecular nanostructure with orbiting spheres"></div>
</div>

<!-- Standards of care -->
<section class="abs standards">
  <svg width="1200" height="410" viewBox="0 0 1200 410" style="position:absolute;left:0;top:0;" aria-hidden="true">
    <defs>
      <linearGradient id="stdCyan" x1="0" y1="0" x2="1" y2="0">
        <stop offset="0" stop-color="#1bb8d8"/><stop offset="1" stop-color="#17d6ea"/>
      </linearGradient>
      <linearGradient id="stdPurple" x1="0" y1="0" x2="1" y2="0">
        <stop offset="0" stop-color="#6a2fc9"/><stop offset="1" stop-color="#9442d8"/>
      </linearGradient>
    </defs>
    <rect width="1200" height="410" fill="url(#stdPurple)"/>
    <path d="M610 0 C560 60 560 120 598 175 C640 235 640 330 600 410 L1200 410 L1200 0 Z" fill="url(#stdCyan)"/>
    <path d="M610 0 C560 60 560 120 598 175 C640 235 640 330 600 410" fill="none" stroke="#07063f" stroke-width="14"/>
    <circle cx="600" cy="190" r="32" fill="#07063f"/>
    <circle cx="600" cy="190" r="20" fill="#4f7fe0"/>
  </svg>
</section>
<h2 class="heading" style="left:142px;top:2718px;">Current<br><strong class="white">standard</strong><br>of care</h2>
<p class="std-copy" style="left:143px;top:2868px;">Sed ut perspiciatis unde omnis iste natus error sit voluptatem accusantiuue laudantium</p>
<a class="btn btn-light" href="#" style="left:143px;top:2945px;width:148px;">Read more</a>
<h2 class="heading" style="left:725px;top:2718px;">Future<br><strong class="ink">standard</strong><br>of care</h2>
<p class="std-copy" style="left:727px;top:2868px;color:#2f5fa0;">Sed ut perspiciatis unde omnis iste natus error sit voluptatem accusantiuue laudantium</p>
<a class="btn btn-dark" href="#" style="left:727px;top:2945px;width:148px;">Read more</a>

<!-- Contact -->
<h2 class="heading" style="left:0;top:3165px;width:1200px;text-align:center;">Contact <strong>us</strong></h2>
<div class="contact-field" style="left:234px;top:3247px;width:359px;">First Name</div>
<div class="contact-field" style="left:606px;top:3247px;width:359px;">Last Name</div>
<div class="contact-field" style="left:234px;top:3312px;width:359px;">Email address</div>
<div class="contact-field" style="left:606px;top:3312px;width:359px;">Phone Number</div>
<div class="contact-field" style="left:234px;top:3377px;width:731px;height:115px;">Message</div>
<div class="abs contact-fade" role="img" aria-label="Flowing light wave lines"></div>
<a class="btn" href="#" style="left:526px;top:3521px;width:148px;">Submit</a>

<!-- Footer -->
<footer class="abs site-footer"></footer>
<div class="abs chat-btn">
  <svg width="30" height="28" viewBox="0 0 30 28" aria-label="Chat">
    <path d="M3 3 H22 V17 H9 L3 22 Z" fill="#fff"/>
    <path d="M24 8 H27 V25 L22 21 H10 V19 H24 Z" fill="#fff"/>
  </svg>
</div>
<div class="brand" style="left:482px;top:3722px;"><span class="brand-dot"></span>LUMIVA</div>
<nav class="footer-nav">
  <a href="#">HOME</a><a href="#">ABOUT</a><a href="#">TECHNOLOGY</a><a href="#">PRESS</a><a href="#">CONTACT</a>
</nav>
<p class="abs copyright">@2025 Companyname. All rights reserved.</p>
<div class="abs social"><span></span><span class="filled"></span></div>

</body>
</html>
```